Flyer für Reifen- und Autoservicebetrieb
Zielgruppe
Wir sind ein Reifen- und Autoservicebetrieb; eine freie KFZ-Meister-Werkstatt ohne Markenbindung.
Aufgabenstellung
Im Focus des Flyers soll auf der Vorderseite der Reifenservice stehen, da dieser zur bevorstehenden Winterreifen-Wechselsaison erscheinen wird (Reifenwechsel, Einlagerung, Räderwäsche, Online-Termin). Auf der Rückseite soll der Autoservice und der 'neu' angebotene LKW- und Landwirtschafts- Reifenservice beworben werden.

```html
<!DOCTYPE html>
<html lang="de">
<head>
<meta charset="utf-8">
<title>Velnor Reifen – Flyer</title>
<link rel="stylesheet" href="https://fonts.googleapis.com/css2?family=Exo+2:wght@300;400;600&family=Saira+Condensed:wght@700&display=swap">
<style>
  :root{
    --stage:#9a9a9a;
    --panel:#d3d3d3;
    --panel-light:#dfe1e3;
    --orange:#f4a41e;
    --ink:#333235;
    --pill:#333235;
    --white:#ffffff;
    --logo-grey:#8f9093;
  }
  *{margin:0;padding:0;box-sizing:border-box}
  html,body{width:1036px;height:1200px;overflow:hidden;background:var(--stage)}
  body{position:relative;font-family:"Exo 2",sans-serif;color:var(--ink)}
  .flyer{position:absolute;top:124px;width:479px;height:975px;background:var(--panel);overflow:hidden;box-shadow:0 4px 12px rgba(0,0,0,.25)}
  .flyer--front{left:28px}
  .flyer--back{left:538px}
  .photo{position:absolute;left:0;top:0;width:479px}
  .brand{position:absolute;top:58px;left:0;width:479px;display:flex;justify-content:center;align-items:center;gap:10px;z-index:3}
  .brand__dot{width:30px;height:30px;border-radius:50%;background:var(--logo-grey)}
  .brand__name{font-family:"Saira Condensed",sans-serif;font-weight:700;font-size:36px;color:var(--orange);letter-spacing:.5px;line-height:1}
  .band{position:absolute;left:0;top:0;z-index:2}
  .headline{position:absolute;left:0;top:436px;width:479px;text-align:center;font-family:"Saira Condensed",sans-serif;font-weight:700;font-size:37px;line-height:42px;color:var(--ink);letter-spacing:-.5px;z-index:3}
  .pill{position:absolute;height:41px;border-radius:21px;background:var(--pill);color:var(--white);font-family:"Exo 2",sans-serif;font-weight:600;display:flex;align-items:center;justify-content:center;z-index:3}
  .pill--front{left:37px;top:577px;width:405px;font-size:17px}
  .pill--back{left:108px;top:365px;width:261px;font-size:19px}
  .services{position:absolute;left:0;width:479px;list-style:none;text-align:center;font-weight:300;font-size:17.5px;color:var(--ink);z-index:3}
  .services--front{top:629px;line-height:23px}
  .services--back{top:423px;line-height:24px}
  .web{position:absolute;left:0;top:915px;width:479px;text-align:center;font-size:15px;letter-spacing:5px;font-weight:400}
  .lower{position:absolute;left:0;top:0;z-index:1}
  .news{position:absolute;left:0;top:710px;width:479px;text-align:center;font-weight:600;font-size:15px;color:var(--ink);z-index:3}
  .arc{position:absolute;left:115px;top:730px;z-index:3}
  .arc text{font-family:"Exo 2",sans-serif;font-weight:600;font-size:23px;fill:var(--ink)}
  .hours{position:absolute;left:0;top:800px;width:479px;text-align:center;z-index:3}
  .hours__title{font-weight:600;font-size:15px;margin-bottom:6px}
  .hours__line{font-weight:300;font-size:15px;line-height:19px}
  .contact{position:absolute;left:0;top:890px;width:479px;text-align:center;font-style:normal;font-weight:400;font-size:15px;line-height:19.5px;letter-spacing:4.5px;z-index:3}
</style>
</head>
<body>

<section class="flyer flyer--front">
  <svg class="photo" width="479" height="400" role="img" aria-label="Foto: Mechaniker mit Handschuhen hält einen Winterreifen zwischen weißen und grauen Autos">
    <defs>
      <linearGradient id="frontPhoto" x1="0" y1="0" x2="0" y2="1">
        <stop offset="0" stop-color="#ffffff"/>
        <stop offset=".35" stop-color="#e4e5e7"/>
        <stop offset="1" stop-color="#9c9ea1"/>
      </linearGradient>
    </defs>
    <rect width="479" height="400" fill="url(#frontPhoto)"/>
  </svg>
  <div class="brand"><span class="brand__dot"></span><span class="brand__name">VELNOR REIFEN</span></div>
  <svg class="band" width="479" height="560">
    <polygon points="0,395 479,395 479,528 239,552 0,528" fill="var(--orange)"/>
  </svg>
  <h1 class="headline">Ihr Experte für hochwertige<br>Reifen und Service</h1>
  <div class="pill pill--front">Wartung und Pflege für IhrE Räder und Reifen</div>
  <ul class="services services--front">
    <li>- Winterreifen</li>
    <li>- Rädereinlagerung</li>
    <li>- Reifenmontage</li>
    <li>- Auswuchten</li>
    <li>- Reifencheck</li>
    <li>- Reifenreparatur</li>
    <li>- Luftdruckkontrolle</li>
    <li>- Kalibrierung des Reifendruckkontrollsystems</li>
    <li>- Räderwäsche</li>
    <li>- Saisonaler Räder-/ Reifenwechsel</li>
    <li>- Online-Termin buchen</li>
  </ul>
  <p class="web">www.velnor-reifen.de</p>
</section>

<section class="flyer flyer--back">
  <svg class="lower" width="479" height="975">
    <polygon points="0,680 239,703 479,680 479,975 0,975" fill="var(--panel-light)"/>
  </svg>
  <svg class="photo" width="479" height="345" role="img" aria-label="Foto: helle Kfz-Werkstatt mit blauer Hebebühne, Werkbänken, Autos und Werkzeug auf dem Boden">
    <defs>
      <linearGradient id="backPhoto" x1="0" y1="0" x2="0" y2="1">
        <stop offset="0" stop-color="#ffffff"/>
        <stop offset=".3" stop-color="#cfd8e4"/>
        <stop offset=".6" stop-color="#4d6fa8"/>
        <stop offset="1" stop-color="#3b3d40"/>
      </linearGradient>
    </defs>
    <polygon points="0,0 479,0 479,318 239,340 0,318" fill="url(#backPhoto)"/>
  </svg>
  <div class="brand"><span class="brand__dot"></span><span class="brand__name">VELNOR REIFEN</span></div>
  <div class="pill pill--back">Unser Kfz-Service</div>
  <ul class="services services--back">
    <li>- Inspektion</li>
    <li>- Ölservice</li>
    <li>- Klimaservice</li>
    <li>- Fehlerdiagnose</li>
    <li>- Stossdämpfer-Service</li>
    <li>- Hauptuntersuchung/ Abgasuntersuchung (HU/AU)</li>
    <li>- Bremsenservice</li>
    <li>- Wintercheck</li>
    <li>- BatTerieservice</li>
    <li>- Fahrzeugreparaturservice</li>
  </ul>
  <p class="news">NEU: Reifenservice für LKW &amp; Landwirtschaft</p>
  <svg class="arc" width="250" height="110">
    <path id="arcPath" d="M8,104 Q125,-50 242,104" fill="none"/>
    <text><textPath href="#arcPath" startOffset="50%" text-anchor="middle">für PKW &amp; Transporter</textPath></text>
  </svg>
  <div class="hours">
    <p class="hours__title">Öffnungszeiten</p>
    <p class="hours__line">Montag - Freitag</p>
    <p class="hours__line">8-12 Uhr und 12:30 - 17 Uhr</p>
  </div>
  <address class="contact">
    Lindweg 12, D-24519 Harkstedt<br>
    Tel.: 04872 315 66 00<br>
    info@velnor-reifen.de
  </address>
</section>

</body>
</html>
```